Review/Re-Design Supermarket E-Commerce website

We have launched our Supermarket E-commerce Website but feel it is lacking a modern feel.

Please re-design the current Supermarket E-commerce site, creating a more modern look and feel.

I am looking for design changes to things such as:

- Fonts
- Button shape & Size
- Shapes of boxes
- Layout of drop down menus
- A new shopping cart / button
- The Header (and in particular the use and positioning of the logo)
- Supplying a generic background image (currently berries)

Please do not change the structure of the page. For instance, the category selection will always be on the left, the items will always be displayed in rows of 3 and the shopping cart should be on the right.
Updates

Current site can be found at www.korvamarketplace.com.au

Project Deadline Extended
Reason: designs coming in are generally too different from current design. we are looking for less that 10% change to the overall look and feel. one aspect that needs a lot of work is the checkout cart on the right hand side. please checkout http://www2.pellingtonfresh.com.au/?gclid=XQWB4pzrhnLDGAKUrTmeYbNVsP

Target Market(s)

Consumers buying their weekly grocery shopping online

Industry/Entity Type

Shopping

Number of Pages Required

1 page

Requirements
Must have
• Stick to the branding of the Logo. Which is Red, Blue and White.
• Other colours may be used in small percentages.
Should not have
• Do not change the Structure of the site.

```html
<!DOCTYPE html>
<html lang="en">
<head>
<meta charset="utf-8">
<title>Korva Marketplace – Online Grocery</title>
<link rel="stylesheet" href="https://fonts.googleapis.com/css2?family=Open+Sans:wght@400;600;700;800&display=swap">
<style>
:root{
  --red:#e41b23;
  --red-dark:#b8131a;
  --blue:#1a3f8f;
  --ink:#222;
  --muted:#777;
  --line:#e4e4e4;
  --soft:#f4f4f4;
  --white:#fff;
}
*{box-sizing:border-box;margin:0;padding:0}
html,body{width:1200px;height:2173px;overflow:hidden;background:var(--white)}
body{font-family:"Open Sans",Arial,sans-serif;color:var(--ink);position:relative}
.abs{position:absolute}

/* header */
.mini-cart{left:1050px;top:12px;display:flex;gap:26px;align-items:flex-start}
.mini-cart .count{font-size:15px;color:var(--muted);text-align:center;line-height:1.1}
.mini-cart .total{text-align:right}
.mini-cart .total span{display:block;font-size:19px;font-weight:600}
.mini-cart .total strong{display:block;font-size:28px;font-weight:400}
.brand{left:22px;top:88px;font-size:43px;font-weight:800;color:var(--blue);letter-spacing:.5px;display:flex;align-items:center;gap:14px}
.brand i{width:26px;height:26px;border-radius:50%;background:var(--red);display:block}
.search{left:575px;top:85px;width:540px;height:60px;border:1px solid var(--line);display:flex;align-items:center;font-size:17px;color:var(--muted)}
.search .field{flex:1;padding-left:18px}
.search .cats{width:130px;border-left:1px solid var(--line);height:100%;display:flex;align-items:center;padding-left:14px}
.search-btn{left:1120px;top:85px;width:58px;height:60px;background:var(--red);display:flex;align-items:center;justify-content:center}

.nav{left:0;top:171px;width:1200px;height:54px;background:var(--red);display:flex;align-items:center}
.nav .home{width:72px;height:54px;margin-left:24px;background:var(--red-dark);display:flex;align-items:center;justify-content:center}
.nav a{position:absolute;color:var(--white);font-size:14px;font-weight:700;text-decoration:none;letter-spacing:.3px}
.nav .sep{position:absolute;top:14px;width:1px;height:26px;background:rgba(255,255,255,.6)}

/* sidebar */
.categories{left:20px;top:255px;width:135px}
.categories h2{font-size:13px;font-weight:700;letter-spacing:.5px;margin-bottom:8px}
.categories li{list-style:none;font-size:15px;color:#444;height:44.5px;line-height:44px;border-bottom:1px solid var(--line);white-space:nowrap}

/* hero */
.hero{left:217px;top:241px;width:736px;height:362px;background:radial-gradient(ellipse at 50% 75%,#f3b43a 0%,#f0d27c 30%,#fbefe0 55%,#fff 75%)}
.dots{left:900px;top:588px;display:flex;gap:5px}
.dots i{width:12px;height:12px;border-radius:50%;background:#999;display:block}
.dots i:last-child{background:#ccc}
.perks{left:217px;top:622px;width:736px;display:flex;justify-content:space-between}
.perk{display:flex;align-items:center;gap:12px;font-size:14px;line-height:1.2;color:#333}

/* products */
.card{width:227px;height:330px;border:1px solid var(--line);background:var(--white)}
.card .photo{position:absolute;left:30px;top:30px;width:167px;height:160px;border-radius:50%}
.photo.red{background:radial-gradient(circle at 40% 35%,#f25a4c,#c61a1a 60%,#8e0d12)}
.photo.dark{background:radial-gradient(circle at 40% 35%,#c22a3c,#8a0e1f 60%,#5e0712)}
.photo.green{background:radial-gradient(circle at 40% 35%,#b6e46a,#6cb92e 60%,#3f8a18)}
.photo.lime{background:radial-gradient(circle at 40% 35%,#e2f3a5,#a8d45a 60%,#6aa82e)}
.card .name{position:absolute;left:10px;top:232px;font-size:13px;font-weight:600;letter-spacing:-.3px}
.card .stars{position:absolute;right:10px;top:228px;font-size:15px;color:#aaa;letter-spacing:2px}
.card .buy{position:absolute;left:0;bottom:0;width:100%;height:50px;background:var(--soft);display:flex;align-items:center;justify-content:space-between;padding:0 10px}
.card .price{font-size:29px;letter-spacing:-1px}
.add{display:flex;align-items:center;height:28px;border:1px solid #ccc;background:var(--white)}
.add span{font-size:8px;font-weight:700;padding:0 7px}
.add b{width:26px;height:28px;background:var(--red);display:flex;align-items:center;justify-content:center}

/* cart panel */
.cart-panel{left:965px;top:241px;width:235px;height:1545px;border-left:1px solid var(--line)}
.collect{left:982px;top:278px;display:flex;flex-direction:column;gap:10px}
.collect .row{display:flex;gap:14px;align-items:flex-start;font-size:11px;line-height:1.3}
.collect strong{font-size:13px;display:block}
.summary{left:982px;top:380px;width:200px;display:flex;align-items:flex-end;gap:10px}
.summary .items{font-size:12px;margin-bottom:8px}
.summary .amt{margin-left:auto;text-align:right;font-size:24px;font-weight:700}
.summary .amt small{display:block;font-size:12px;font-weight:400;text-align:right;border-top:1px solid #ccc;margin-top:2px}
.checkout{left:982px;top:451px;width:200px;height:46px;border:1px solid #bbb;display:flex;align-items:center}
.checkout span{flex:1;text-align:center;font-size:14px;font-weight:700;letter-spacing:.5px}
.checkout b{width:50px;height:46px;background:var(--red);display:flex;align-items:center;justify-content:center;margin-right:-1px}
.line-item{left:982px;width:200px;font-size:12px}
.line-item p{display:flex;justify-content:space-between}
.line-item strong{display:block;font-size:22px;font-weight:400;color:#555;margin-top:4px}

/* footer */
.footer-col{top:1860px}
.footer-col h3{font-size:23px;font-weight:400;color:#444;margin-bottom:8px}
.footer-col li{list-style:none;font-size:12px;line-height:24.5px;color:#444}
.badge{width:120px;height:38px;border-radius:5px;background:#222;margin-bottom:14px}
.copyright{left:0;top:2112px;width:1200px;text-align:center;font-size:13px;color:#555}
</style>
</head>
<body>

<header>
  <div class="abs mini-cart">
    <div class="count">
      <svg width="32" height="28" viewBox="0 0 32 28"><path d="M2 3h5l4 15h15l3-10H9" fill="none" stroke="#333" stroke-width="2"/><circle cx="13" cy="23" r="2.2" fill="#333"/><circle cx="24" cy="23" r="2.2" fill="#333"/></svg>
      <div>0 items</div>
    </div>
    <div class="total"><span>Total</span><strong>$0.00</strong></div>
  </div>

  <div class="abs brand">KORVA MARKETPLACE <i></i></div>

  <div class="abs search">
    <div class="field">Search your fruit here</div>
    <div class="cats">All Categories ⌄</div>
  </div>
  <div class="abs search-btn">
    <svg width="24" height="24" viewBox="0 0 24 24"><circle cx="10" cy="10" r="7" fill="none" stroke="#fff" stroke-width="3"/><path d="M15 15l7 7" stroke="#fff" stroke-width="3"/></svg>
  </div>

  <nav class="abs nav">
    <div class="home"><svg width="22" height="20" viewBox="0 0 22 20"><path d="M11 1L1 10h3v9h5v-6h4v6h5v-9h3z" fill="#fff"/></svg></div>
    <a style="left:116px">PRODUCTS</a><span class="sep" style="left:228px"></span>
    <a style="left:255px">LOGIN</a><span class="sep" style="left:342px"></span>
    <a style="left:382px">REGISTER</a><span class="sep" style="left:497px"></span>
    <a style="left:530px">MY ACCOUNT</a><span class="sep" style="left:660px"></span>
    <a style="left:697px">MY CART</a><span class="sep" style="left:800px"></span>
  </nav>
</header>

<aside class="abs categories">
  <h2>CATEGORIES</h2>
  <ul>
    <li>Baby</li><li>Accessories</li><li>Bakery</li><li>Biscuits &amp; Cookies</li><li>Baking Needs</li>
    <li>Baking Accessories</li><li>Beverages</li><li>Coconut</li><li>Biscuits</li><li>Biscuits</li>
    <li>Breakfast Foods</li><li>Cereal</li><li>Canned Food</li><li>Baked Beans</li><li>Cheese</li>
    <li>Blocks</li><li>Chilled Foods</li><li>Bacon</li><li>Chips</li><li>Burger Rings</li>
    <li>Condiments</li><li>Antipasto</li><li>Confectionery</li><li>Chews</li><li>Cooking Needs</li>
    <li>Breadcrumbs &amp; Coatings</li><li>Desserts</li><li>Creamed Rice</li><li>Frozen Food</li><li>Asian</li>
    <li>Fruit</li><li>Apples</li>
  </ul>
</aside>

<main>
  <div class="abs hero" role="img" aria-label="Banner photo of a baby sitting behind a pile of fresh fruit"></div>
  <div class="abs dots"><i></i><i></i><i></i></div>

  <div class="abs perks">
    <div class="perk"><svg width="22" height="26" viewBox="0 0 22 26"><circle cx="11" cy="9" r="7" fill="none" stroke="#222" stroke-width="2.5"/><path d="M6 15l-2 9 7-3 7 3-2-9" fill="none" stroke="#222" stroke-width="2"/></svg><span>100% Satisfaction<br>Guarantee</span></div>
    <div class="perk"><svg width="24" height="24" viewBox="0 0 24 24"><circle cx="12" cy="12" r="9" fill="none" stroke="#222" stroke-width="2.5"/><path d="M12 7v5l3 3" stroke="#222" stroke-width="2" fill="none"/></svg><span>24/7<br>Free Support</span></div>
    <div class="perk"><svg width="24" height="20" viewBox="0 0 24 20"><rect x="2" y="4" width="20" height="14" rx="2" fill="#222"/><rect x="8" y="1" width="8" height="4" fill="#222"/><circle cx="12" cy="11" r="4" fill="#fff"/></svg><span>Stock Photos<br>Included</span></div>
    <div class="perk"><svg width="22" height="26" viewBox="0 0 22 26"><circle cx="11" cy="9" r="7" fill="none" stroke="#222" stroke-width="2.5"/><path d="M6 15l-2 9 7-3 7 3-2-9" fill="none" stroke="#222" stroke-width="2"/></svg><span>100% Satisfaction<br>Guarantee</span></div>
  </div>

  <section class="products">
    <article class="abs card" style="left:217px;top:683px"><div class="photo red" role="img" aria-label="Single red apple"></div><div class="name">Apples Red 2kg Bag</div><div class="stars">☆☆☆☆</div><div class="buy"><span class="price">$8.39</span><span class="add"><span>ADD TO CART</span><b><svg width="14" height="12" viewBox="0 0 14 12"><path d="M0 1h3l2 7h7l1-5H4" fill="none" stroke="#fff" stroke-width="1.5"/><circle cx="6" cy="10.5" r="1" fill="#fff"/><circle cx="11" cy="10.5" r="1" fill="#fff"/></svg></b></span></div></article>
    <article class="abs card" style="left:471px;top:683px"><div class="photo green" role="img" aria-label="Two green apples"></div><div class="name">Apples Red 2kg Bag</div><div class="stars">☆☆☆☆</div><div class="buy"><span class="price">$8.39</span><span class="add"><span>ADD TO CART</span><b><svg width="14" height="12" viewBox="0 0 14 12"><path d="M0 1h3l2 7h7l1-5H4" fill="none" stroke="#fff" stroke-width="1.5"/><circle cx="6" cy="10.5" r="1" fill="#fff"/><circle cx="11" cy="10.5" r="1" fill="#fff"/></svg></b></span></div></article>
    <article class="abs card" style="left:724px;top:683px"><div class="photo dark" role="img" aria-label="Pair of dark red apples"></div><div class="name">Apples Red 2kg Bag</div><div class="stars">☆☆☆☆</div><div class="buy"><span class="price">$8.39</span><span class="add"><span>ADD TO CART</span><b><svg width="14" height="12" viewBox="0 0 14 12"><path d="M0 1h3l2 7h7l1-5H4" fill="none" stroke="#fff" stroke-width="1.5"/><circle cx="6" cy="10.5" r="1" fill="#fff"/><circle cx="11" cy="10.5" r="1" fill="#fff"/></svg></b></span></div></article>

    <article class="abs card" style="left:217px;top:1040px"><div class="photo green" role="img" aria-label="Bunch of green apples"></div><div class="name">Apples Red 2kg Bag</div><div class="stars">☆☆☆☆</div><div class="buy"><span class="price">$8.39</span><span class="add"><span>ADD TO CART</span><b><svg width="14" height="12" viewBox="0 0 14 12"><path d="M0 1h3l2 7h7l1-5H4" fill="none" stroke="#fff" stroke-width="1.5"/><circle cx="6" cy="10.5" r="1" fill="#fff"/><circle cx="11" cy="10.5" r="1" fill="#fff"/></svg></b></span></div></article>
    <article class="abs card" style="left:471px;top:1040px"><div class="photo dark" role="img" aria-label="Red apple with a leaf"></div><div class="name">Apples Red 2kg Bag</div><div class="stars">☆☆☆☆</div><div class="buy"><span class="price">$8.39</span><span class="add"><span>ADD TO CART</span><b><svg width="14" height="12" viewBox="0 0 14 12"><path d="M0 1h3l2 7h7l1-5H4" fill="none" stroke="#fff" stroke-width="1.5"/><circle cx="6" cy="10.5" r="1" fill="#fff"/><circle cx="11" cy="10.5" r="1" fill="#fff"/></svg></b></span></div></article>
    <article class="abs card" style="left:724px;top:1040px"><div class="photo red" role="img" aria-label="Small red apple" style="left:58px;top:55px;width:111px;height:110px"></div><div class="name">Apples Red 2kg Bag</div><div class="stars">☆☆☆☆</div><div class="buy"><span class="price">$8.39</span><span class="add"><span>ADD TO CART</span><b><svg width="14" height="12" viewBox="0 0 14 12"><path d="M0 1h3l2 7h7l1-5H4" fill="none" stroke="#fff" stroke-width="1.5"/><circle cx="6" cy="10.5" r="1" fill="#fff"/><circle cx="11" cy="10.5" r="1" fill="#fff"/></svg></b></span></div></article>

    <article class="abs card" style="left:217px;top:1398px"><div class="photo dark" role="img" aria-label="Row of three red apples"></div><div class="name">Apples Red 2kg Bag</div><div class="stars">☆☆☆☆</div><div class="buy"><span class="price">$8.39</span><span class="add"><span>ADD TO CART</span><b><svg width="14" height="12" viewBox="0 0 14 12"><path d="M0 1h3l2 7h7l1-5H4" fill="none" stroke="#fff" stroke-width="1.5"/><circle cx="6" cy="10.5" r="1" fill="#fff"/><circle cx="11" cy="10.5" r="1" fill="#fff"/></svg></b></span></div></article>
    <article class="abs card" style="left:471px;top:1398px"><div class="photo red" role="img" aria-label="Group of red apples"></div><div class="name">Apples Red 2kg Bag</div><div class="stars">☆☆☆☆</div><div class="buy"><span class="price">$8.39</span><span class="add"><span>ADD TO CART</span><b><svg width="14" height="12" viewBox="0 0 14 12"><path d="M0 1h3l2 7h7l1-5H4" fill="none" stroke="#fff" stroke-width="1.5"/><circle cx="6" cy="10.5" r="1" fill="#fff"/><circle cx="11" cy="10.5" r="1" fill="#fff"/></svg></b></span></div></article>
    <article class="abs card" style="left:724px;top:1398px"><div class="photo lime" role="img" aria-label="Single green apple with a leaf"></div><div class="name">Apples Red 2kg Bag</div><div class="stars">☆☆☆☆</div><div class="buy"><span class="price">$8.39</span><span class="add"><span>ADD TO CART</span><b><svg width="14" height="12" viewBox="0 0 14 12"><path d="M0 1h3l2 7h7l1-5H4" fill="none" stroke="#fff" stroke-width="1.5"/><circle cx="6" cy="10.5" r="1" fill="#fff"/><circle cx="11" cy="10.5" r="1" fill="#fff"/></svg></b></span></div></article>
  </section>
</main>

<aside>
  <div class="abs cart-panel"></div>
  <div class="abs collect">
    <div class="row"><svg width="26" height="24" viewBox="0 0 26 24"><path d="M3 8h20l-2 14H5z" fill="#222"/><path d="M8 8a5 5 0 0110 0" fill="none" stroke="#222" stroke-width="2"/></svg><div><strong>Click &amp; Collect</strong>12 Harbour Lane<br>Korva TAS 7000</div></div>
    <div class="row"><svg width="26" height="18" viewBox="0 0 26 18"><rect x="1" y="2" width="15" height="11" fill="#222"/><path d="M16 6h5l4 4v3h-9z" fill="#222"/><circle cx="6" cy="15" r="2.5" fill="#222"/><circle cx="20" cy="15" r="2.5" fill="#222"/></svg><div>Delivery info</div></div>
  </div>
  <div class="abs summary">
    <svg width="44" height="40" viewBox="0 0 44 40"><path d="M2 4h7l6 22h21l5-16H12" fill="none" stroke="#222" stroke-width="3.5"/><circle cx="18" cy="34" r="3.5" fill="#222"/><circle cx="33" cy="34" r="3.5" fill="#222"/></svg>
    <span class="items">4 items</span>
    <span class="amt">$ 17.98<small>Total</small></span>
  </div>
  <div class="abs checkout"><span>CHECKOUT</span><b><svg width="24" height="22" viewBox="0 0 24 22"><path d="M1 2h4l3 11h12l3-8H7" fill="none" stroke="#fff" stroke-width="2.2"/><circle cx="10" cy="18" r="2" fill="#fff"/><circle cx="18" cy="18" r="2" fill="#fff"/></svg></b></div>

  <div class="abs line-item" style="top:522px"><p><span>1 X Fuji Apples Each</span><span>⊠</span></p><strong>$0.60</strong></div>
  <div class="abs line-item" style="top:595px"><p><span>1 X Green Apples Each</span><span>⊠</span></p><strong>$0.60</strong></div>
  <div class="abs line-item" style="top:668px"><p><span>2 X Apples Red 2kg Bag</span><span>⊠</span></p><strong>$16.78</strong></div>
</aside>

<footer>
  <div class="abs footer-col" style="left:135px"><h3>Events</h3><ul><li>Anniversary</li><li>Baby Shower</li><li>Birthday</li><li>Christmas Party</li><li>New Year Party</li></ul></div>
  <div class="abs footer-col" style="left:384px"><h3>My account</h3><ul><li>My orders</li><li>My merchandise</li><li>My credit slips</li><li>My addresses</li><li>My personal info</li></ul></div>
  <div class="abs footer-col" style="left:673px"><h3>Information</h3><ul><li>Specials</li><li>New products</li><li>Best seller</li><li>Contact us</li><li>Page configuration</li></ul></div>
  <div class="abs footer-col" style="left:920px"><h3>Download apps</h3><div class="badge"></div><div class="badge"></div></div>
  <p class="abs copyright">© Tallow Pty Ltd 2014 - All Rights Reserved ver 1.1.2</p>
</footer>

</body>
</html>
```